Web page design for podiatry office*

Need a web page for our podiatry office. It should feature most of our services, hours, directions and location. Should include a short bio of the doctor and a contact page.

Coding

Coded - Design and coding required

Number of Pages Required

1 page

Colors

Designer to choose colors to be used in the design.

```html
<!DOCTYPE html>
<html lang="en">
<head>
<meta charset="utf-8">
<title>Podiatry – Foot &amp; Ankle Care</title>
<link href="https://fonts.googleapis.com/css2?family=Roboto:wght@300;400;500;700&family=Open+Sans:wght@400;600;700&display=swap" rel="stylesheet">
<style>
:root{
  --green:#8cc63f;
  --green-dark:#6ea52a;
  --green-soft:#c9e59a;
  --brown:#3a2d28;
  --brown-deep:#2a201c;
  --ink:#2f2f2f;
  --muted:#777;
  --grey-bg:#eeeeee;
  --white:#ffffff;
}
*{box-sizing:border-box;margin:0;padding:0}
html,body{width:1200px;height:3488px;overflow:hidden}
body{font-family:"Open Sans",Arial,sans-serif;color:var(--ink);background:var(--white);position:relative}
h1,h2,h3{font-family:"Roboto",Arial,sans-serif}
.section{position:relative;width:1200px;overflow:hidden}
.abs{position:absolute}

/* ---------- hero ---------- */
.hero{height:520px;background:linear-gradient(180deg,#e4e4e4 0%,#f3f3f3 100%)}
.topbar{position:absolute;top:0;left:0;width:1200px;height:40px;font-size:12px;color:#555;display:flex;align-items:center;padding:0 250px;justify-content:space-between;z-index:3}
.topbar span{display:inline-flex;align-items:center;gap:6px;margin-right:22px}
.topbar svg{width:12px;height:12px}
.hero-photo{position:absolute;left:560px;top:0;width:640px;height:430px;background:radial-gradient(ellipse at 60% 45%,#f1d6c4 0%,#e2bfa8 35%,#d9d9d9 75%,#e6e6e6 100%)}
.brand{position:absolute;left:240px;top:36px;display:flex;align-items:center;gap:10px;z-index:3}
.brand-dot{width:18px;height:18px;border-radius:50%;background:var(--green)}
.brand-name{font-family:"Roboto",sans-serif;font-weight:500;font-size:26px;letter-spacing:3px;color:var(--brown)}
.nav{position:absolute;right:250px;top:70px;display:flex;gap:26px;font-size:14px;color:#444;z-index:3}
.nav a{color:inherit;text-decoration:none}
.hero-copy{position:absolute;left:240px;top:168px;width:430px;z-index:3}
.hero-copy h1{font-size:30px;line-height:38px;font-weight:700;color:var(--ink)}
.hero-copy p{margin-top:12px;font-size:14px;line-height:21px;color:#555}
.hero-wave{position:absolute;left:0;bottom:0;width:1200px;height:160px}

/* ---------- welcome ---------- */
.welcome{height:380px}
.doctor-ring{position:absolute;left:236px;top:10px;width:300px;height:300px;border-radius:50%;border:8px solid #f2f2f2;box-shadow:0 4px 18px rgba(0,0,0,.12);background:var(--white)}
.doctor-photo{position:absolute;inset:8px;border-radius:50%;background:linear-gradient(180deg,#d9dde2 0%,#e9ecef 50%,#f5f6f8 100%)}
.welcome-text{position:absolute;left:612px;top:20px;width:360px}
.welcome-text h2{font-size:26px;font-weight:400;color:var(--ink)}
.welcome-text h2 em{font-style:normal;color:var(--green)}
.welcome-text p{margin-top:12px;font-size:12px;line-height:18px;color:#555}
.welcome-text .accent{color:var(--green-dark);font-weight:600;margin-top:12px}
.btn-dark{display:inline-block;margin-top:14px;background:var(--brown);color:var(--white);font-size:11px;padding:8px 18px;border-radius:14px}

/* ---------- services ---------- */
.services{height:600px}
.services-bg{position:absolute;left:0;top:0;width:1200px;height:600px}
.services-head{position:absolute;top:150px;width:1200px;text-align:center}
.services-head h2{font-size:28px;font-weight:700;color:var(--ink)}
.services-head h2 em{font-style:normal;font-weight:300;color:var(--green)}
.services-head p{margin-top:8px;font-size:13px;color:var(--muted)}
.cards{position:absolute;top:360px;left:112px;display:flex;gap:26px}
.card{width:176px;height:180px;background:var(--white);border-radius:8px;box-shadow:0 4px 14px rgba(0,0,0,.1);text-align:center;padding:18px 14px}
.card.raised{transform:translateY(-6px);box-shadow:0 8px 22px rgba(0,0,0,.16)}
.card svg{width:44px;height:44px}
.card h3{margin-top:10px;font-size:17px;font-weight:500;color:var(--ink)}
.card p{margin-top:8px;font-size:10.5px;line-height:15px;color:var(--muted)}
.dots{position:absolute;top:570px;width:1200px;display:flex;justify-content:center;gap:6px}
.dots i{width:7px;height:7px;border-radius:50%;background:#bbb}
.dots i.on{background:#777}

/* ---------- hours ---------- */
.hours{height:360px}
.care-photo{position:absolute;left:248px;top:20px;width:344px;height:232px;background:linear-gradient(135deg,#3b3330 0%,#6d4a45 40%,#c63a4e 60%,#5a4a44 100%)}
.hours-note{position:absolute;left:248px;top:262px;width:344px;font-size:11px;line-height:16px;color:#444}
.hours-note b{color:var(--ink)}
.hours-card{position:absolute;left:688px;top:28px;width:264px;height:300px;background:var(--green);border-radius:10px;padding:26px 28px;color:var(--white);box-shadow:0 6px 16px rgba(0,0,0,.12)}
.hours-card h3{font-size:24px;font-weight:500}
.hours-card ul{list-style:none;margin-top:20px}
.hours-card li{font-size:12px;line-height:26px;display:flex;align-items:center;gap:8px}
.hours-card li::before{content:"";width:5px;height:5px;border-radius:50%;background:var(--white)}

/* ---------- testimonial ---------- */
.testimonial{height:520px}
.testimonial-bg{position:absolute;left:0;top:0;width:1200px;height:520px}
.quote{position:absolute;left:300px;top:300px;width:600px;text-align:center;color:var(--white)}
.quote p{font-size:18px;line-height:28px;font-weight:400}
.quote cite{display:block;margin-top:22px;font-size:11px;font-style:normal;color:#cfc6c1}
.arrow{position:absolute;top:330px;width:30px;height:30px;border-radius:50%;border:2px solid var(--white);display:flex;align-items:center;justify-content:center}
.arrow svg{width:12px;height:12px}

/* ---------- directions ---------- */
.directions{height:610px}
.directions h2{position:absolute;top:52px;width:1200px;text-align:center;font-size:28px;font-weight:700}
.map{position:absolute;left:256px;top:112px;width:684px;height:390px;border-radius:4px;box-shadow:0 6px 20px rgba(0,0,0,.18);background:linear-gradient(120deg,#dfe6d8 0%,#e9ece4 35%,#9fc2e6 55%,#b8d3ee 70%,#e3e7dc 100%)}
.map-pin{position:absolute;width:30px;height:40px}
.direction-note{position:absolute;left:328px;top:452px;width:544px;height:150px;background:var(--green);border-radius:8px;padding:26px 40px;text-align:center;color:var(--white);font-size:15px;line-height:22px;font-weight:600}

/* ---------- locations ---------- */
.locations{height:140px}
.loc-grid{position:absolute;left:280px;top:16px;display:grid;grid-template-columns:repeat(4,160px);column-gap:0}
.loc-grid ul{list-style:none}
.loc-grid li{font-size:10px;line-height:17px;color:#555;display:flex;align-items:center;gap:6px}
.loc-grid li::before{content:"";width:4px;height:4px;background:var(--green);border-radius:50%}

/* ---------- footer ---------- */
.footer{height:358px;background:var(--brown-deep)}
.footer-bg{position:absolute;left:0;top:0;width:1200px;height:358px}
.footer-brand{position:absolute;left:540px;top:60px;width:120px;height:120px;border-radius:50%;background:var(--white);display:flex;flex-direction:column;align-items:center;justify-content:center;gap:6px}
.footer-brand .brand-dot{width:14px;height:14px}
.footer-brand span{font-family:"Roboto",sans-serif;font-weight:500;font-size:17px;letter-spacing:2px;color:var(--brown)}
.contact-row{position:absolute;top:196px;left:0;width:1200px;display:flex;justify-content:center;gap:210px}
.contact-item{display:flex;flex-direction:column;align-items:center;gap:8px;color:#ddd;font-size:11px;width:170px;text-align:center}
.contact-item .ic{width:30px;height:30px;border-radius:50%;border:2px solid var(--green);display:flex;align-items:center;justify-content:center}
.contact-item svg{width:14px;height:14px}
.footer-nav{position:absolute;top:296px;width:1200px;display:flex;justify-content:center;gap:22px;font-size:10px;color:#ccc}
.footer-bottom{position:absolute;top:326px;left:0;width:1200px;height:32px;border-top:1px solid rgba(255,255,255,.08);display:flex;align-items:center;justify-content:space-between;padding:0 250px;font-size:9px;color:#aaa}
.social{display:flex;gap:8px}
.social i{width:14px;height:14px;border-radius:50%;background:var(--green)}
</style>
</head>
<body>

<!-- HERO -->
<header class="section hero">
  <div class="hero-photo" role="img" aria-label="Photo of a podiatrist examining a patient's bare foot"></div>
  <div class="topbar">
    <div>
      <span><svg viewBox="0 0 24 24"><path fill="#8cc63f" d="M12 2a7 7 0 0 0-7 7c0 5 7 13 7 13s7-8 7-13a7 7 0 0 0-7-7zm0 9.5A2.5 2.5 0 1 1 12 6.5a2.5 2.5 0 0 1 0 5z"/></svg>485 Orchard Lane, Fairview 10234</span>
      <span><svg viewBox="0 0 24 24"><path fill="#8cc63f" d="M6.6 10.8a15 15 0 0 0 6.6 6.6l2.2-2.2c.3-.3.7-.4 1-.2 1.1.4 2.3.6 3.6.6.6 0 1 .4 1 1V20c0 .6-.4 1-1 1C10.6 21 3 13.4 3 4c0-.6.4-1 1-1h3.5c.6 0 1 .4 1 1 0 1.3.2 2.5.6 3.6.1.3 0 .7-.2 1z"/></svg>(555) 014-2281</span>
    </div>
    <div><span>Monday – Friday 8:00am – 5:00pm, Saturday &amp; Sunday Closed</span></div>
  </div>
  <div class="brand"><div class="brand-dot"></div><div class="brand-name">PODIATRY</div></div>
  <nav class="nav"><a href="#">Home</a><a href="#">About Us</a><a href="#">Our Services</a><a href="#">Contact Us</a></nav>
  <div class="hero-copy">
    <h1>There are a variety of reasons why you may need to see a foot doctor.</h1>
    <p>Lorem Ipsum is simply dummy text of the printing and typesetting industry.</p>
  </div>
  <svg class="hero-wave" viewBox="0 0 1200 160" preserveAspectRatio="none">
    <path d="M0 40 C200 110 380 20 600 70 C820 120 1000 30 1200 60 L1200 160 L0 160Z" fill="#c9e59a"/>
    <path d="M0 70 C220 130 420 40 620 90 C840 140 1020 60 1200 80 L1200 160 L0 160Z" fill="#8cc63f"/>
    <path d="M0 100 C240 150 440 80 640 115 C860 150 1030 95 1200 110 L1200 160 L0 160Z" fill="#ffffff"/>
  </svg>
</header>

<!-- WELCOME -->
<section class="section welcome">
  <div class="doctor-ring"><div class="doctor-photo" role="img" aria-label="Portrait of the podiatrist in a white coat with a stethoscope"></div></div>
  <div class="welcome-text">
    <h2>Welcome <em>to Podiatry</em></h2>
    <p>At Podiatry our team is focused on caring for every patient with warmth and attention. Our offices are designed to provide you with everything you need to leave your visit comfortable and confident in your recovery, with clear guidance at every step.</p>
    <p>Lorem Ipsum is simply dummy text of the printing and typesetting industry. Lorem Ipsum has been the industry's standard dummy text ever since the 1500s, when an unknown printer took a galley of type and scrambled it to make a type specimen book. It has survived not only five centuries, but also the leap into electronic typesetting, remaining essentially unchanged.</p>
    <p class="accent">Come and see in for yourself!</p>
    <span class="btn-dark">Read More</span>
  </div>
</section>

<!-- SERVICES -->
<section class="section services">
  <svg class="services-bg" viewBox="0 0 1200 600" preserveAspectRatio="none">
    <path d="M0 80 C250 20 450 120 700 70 C900 30 1050 90 1200 60 L1200 560 C1000 600 800 520 600 560 C380 600 200 530 0 570Z" fill="#eeeeee"/>
    <path d="M0 330 C300 290 700 380 1200 320" stroke="#8cc63f" stroke-width="3" fill="none"/>
  </svg>
  <div class="services-head">
    <h2>Our Serives <em>Podiatry</em></h2>
    <p>Lorem Ipsum is simply dummy text of the printing and typesetting industry.</p>
  </div>
  <div class="cards">
    <article class="card">
      <svg viewBox="0 0 44 44"><ellipse cx="22" cy="28" rx="9" ry="13" fill="#8cc63f"/><circle cx="15" cy="10" r="3" fill="#8cc63f"/><circle cx="21" cy="7" r="3" fill="#8cc63f"/><circle cx="27" cy="9" r="2.5" fill="#8cc63f"/><circle cx="31" cy="13" r="2" fill="#8cc63f"/></svg>
      <h3>Achilles Tendonitis</h3>
      <p>Lorem Ipsum is simply dummy text of the printing and typesetting industry.</p>
    </article>
    <article class="card">
      <svg viewBox="0 0 44 44"><ellipse cx="22" cy="28" rx="9" ry="13" fill="#8cc63f"/><circle cx="15" cy="10" r="3" fill="#8cc63f"/><circle cx="21" cy="7" r="3" fill="#8cc63f"/><circle cx="27" cy="9" r="2.5" fill="#8cc63f"/><circle cx="31" cy="13" r="2" fill="#8cc63f"/></svg>
      <h3>Arthritis</h3>
      <p>Lorem Ipsum has been the industry's standard dummy text ever since the 1500s, when an printer took a galley.</p>
    </article>
    <article class="card raised">
      <svg viewBox="0 0 44 44"><ellipse cx="22" cy="28" rx="9" ry="13" fill="#8cc63f"/><circle cx="15" cy="10" r="3" fill="#8cc63f"/><circle cx="21" cy="7" r="3" fill="#8cc63f"/><circle cx="27" cy="9" r="2.5" fill="#8cc63f"/><circle cx="31" cy="13" r="2" fill="#8cc63f"/></svg>
      <h3>Brachymetatarsia</h3>
      <p>Lorem Ipsum is simply dummy text of the printing and typesetting industry.</p>
    </article>
    <article class="card">
      <svg viewBox="0 0 44 44"><ellipse cx="22" cy="28" rx="9" ry="13" fill="#8cc63f"/><circle cx="15" cy="10" r="3" fill="#8cc63f"/><circle cx="21" cy="7" r="3" fill="#8cc63f"/><circle cx="27" cy="9" r="2.5" fill="#8cc63f"/><circle cx="31" cy="13" r="2" fill="#8cc63f"/></svg>
      <h3>Flatfoot</h3>
      <p>Lorem Ipsum has been the industry's standard dummy text ever since the 1500s, when an printer took a galley.</p>
    </article>
    <article class="card">
      <svg viewBox="0 0 44 44"><ellipse cx="22" cy="28" rx="9" ry="13" fill="#8cc63f"/><circle cx="15" cy="10" r="3" fill="#8cc63f"/><circle cx="21" cy="7" r="3" fill="#8cc63f"/><circle cx="27" cy="9" r="2.5" fill="#8cc63f"/><circle cx="31" cy="13" r="2" fill="#8cc63f"/></svg>
      <h3>Hallux Rigidus</h3>
      <p>Lorem Ipsum is simply dummy text of the printing and typesetting industry.</p>
    </article>
  </div>
  <div class="dots"><i></i><i class="on"></i><i></i><i></i></div>
</section>

<!-- HOURS -->
<section class="section hours">
  <div class="care-photo" role="img" aria-label="Close-up of a gloved hand treating a patient's foot"></div>
  <p class="hours-note"><b>Lorem Ipsum has been</b> the industry's standard dummy text ever since the 1500s, when an unknown printer took a galley of type and scrambled it to make a type specimen book. It has survived not only five centuries, but also the leap into electronic typesetting, remaining essentially unchanged.</p>
  <div class="hours-card">
    <h3>Business Hours</h3>
    <ul>
      <li>Monday 8:00am – 5:00pm</li>
      <li>Tuesday 8:00am – 5:00pm</li>
      <li>Wednesday 8:00am – 5:00pm</li>
      <li>Thursday 8:00am – 5:00pm</li>
      <li>Friday 8:00am – 5:00pm</li>
      <li>Saturday Closed</li>
      <li>Sunday Closed</li>
    </ul>
  </div>
</section>

<!-- TESTIMONIAL -->
<section class="section testimonial">
  <svg class="testimonial-bg" viewBox="0 0 1200 520" preserveAspectRatio="none" role="img" aria-label="Dark photo backdrop of feet resting on a floor">
    <defs><linearGradient id="tg" x1="0" y1="0" x2="1" y2="1"><stop offset="0" stop-color="#4a3a33"/><stop offset=".5" stop-color="#3a2d28"/><stop offset="1" stop-color="#2b211d"/></linearGradient></defs>
    <path d="M0 150 C200 60 420 170 640 100 C860 30 1020 130 1200 80 L1200 470 C980 520 780 430 560 480 C340 530 170 450 0 490Z" fill="url(#tg)"/>
    <path d="M0 160 C200 70 420 180 640 110 C860 40 1020 140 1200 90" stroke="#ffffff" stroke-opacity=".5" stroke-width="2" fill="none"/>
  </svg>
  <div class="arrow" style="left:250px"><svg viewBox="0 0 12 12"><path d="M8 1 3 6l5 5" stroke="#fff" stroke-width="2" fill="none"/></svg></div>
  <div class="arrow" style="left:920px"><svg viewBox="0 0 12 12"><path d="M4 1l5 5-5 5" stroke="#fff" stroke-width="2" fill="none"/></svg></div>
  <blockquote class="quote">
    <p>Lorem Ipsum has been the industry's standard dummy text ever since the 1500s, when an unknown printer took a galley of type and scrambled it to make a type specimen book.</p>
    <cite>Dana Whitfield</cite>
  </blockquote>
</section>

<!-- DIRECTIONS -->
<section class="section directions">
  <h2>Directions</h2>
  <div class="map" role="img" aria-label="Street map showing the office location">
    <svg class="map-pin" style="left:620px;top:70px" viewBox="0 0 30 40"><path d="M15 0a14 14 0 0 0-14 14c0 10 14 26 14 26s14-16 14-26A14 14 0 0 0 15 0z" fill="#3a2d28"/><circle cx="15" cy="14" r="5" fill="#fff"/></svg>
    <svg class="map-pin" style="left:70px;top:200px" viewBox="0 0 30 40"><path d="M15 0a14 14 0 0 0-14 14c0 10 14 26 14 26s14-16 14-26A14 14 0 0 0 15 0z" fill="#3a2d28"/><circle cx="15" cy="14" r="5" fill="#fff"/></svg>
  </div>
  <div class="direction-note">Lorem Ipsum is simply dummy text of the printing and typesetting industry. Lorem Ipsum has been the industry's standard dummy text ever since the 1500s, when an unknown printer took a galley of type and scrambled it to make a type specimen book.</div>
</section>

<!-- LOCATIONS -->
<section class="section locations">
  <div class="loc-grid">
    <ul><li>Podiatry location</li><li>Podiatry location</li><li>Podiatry location</li><li>Podiatry location</li><li>Podiatry location</li><li>Podiatry location</li></ul>
    <ul><li>Podiatry location</li><li>Podiatry location</li><li>Podiatry location</li><li>Podiatry location</li><li>Podiatry location</li><li>Podiatry location</li></ul>
    <ul><li>Podiatry location</li><li>Podiatry location</li><li>Podiatry location</li><li>Podiatry location</li><li>Podiatry location</li><li>Podiatry location</li></ul>
    <ul><li>Podiatry location</li><li>Podiatry location</li><li>Podiatry location</li><li>Podiatry location</li><li>Podiatry location</li><li>Podiatry location</li></ul>
  </div>
</section>

<!-- FOOTER -->
<footer class="section footer">
  <svg class="footer-bg" viewBox="0 0 1200 358" preserveAspectRatio="none">
    <path d="M0 0 L1200 0 L1200 30 C1000 70 800 10 600 40 C400 70 200 20 0 50Z" fill="#ffffff"/>
  </svg>
  <div class="footer-brand"><div class="brand-dot"></div><span>PODIATRY</span></div>
  <div class="contact-row">
    <div class="contact-item"><div class="ic"><svg viewBox="0 0 24 24"><path fill="#8cc63f" d="M12 2a7 7 0 0 0-7 7c0 5 7 13 7 13s7-8 7-13a7 7 0 0 0-7-7zm0 9.5A2.5 2.5 0 1 1 12 6.5a2.5 2.5 0 0 1 0 5z"/></svg></div>485 Orchard Lane, Fairview 10234</div>
    <div class="contact-item"><div class="ic"><svg viewBox="0 0 24 24"><path fill="#8cc63f" d="M6.6 10.8a15 15 0 0 0 6.6 6.6l2.2-2.2c.3-.3.7-.4 1-.2 1.1.4 2.3.6 3.6.6.6 0 1 .4 1 1V20c0 .6-.4 1-1 1C10.6 21 3 13.4 3 4c0-.6.4-1 1-1h3.5c.6 0 1 .4 1 1 0 1.3.2 2.5.6 3.6.1.3 0 .7-.2 1z"/></svg></div>(555) 014-2281</div>
    <div class="contact-item"><div class="ic"><svg viewBox="0 0 24 24"><rect x="3" y="5" width="18" height="14" rx="2" fill="none" stroke="#8cc63f" stroke-width="2"/><path d="M3 7l9 6 9-6" fill="none" stroke="#8cc63f" stroke-width="2"/></svg></div>hello@stepwellfeet.com</div>
  </div>
  <nav class="footer-nav"><span>Home</span><span>About Us</span><span>Services</span><span>Contact Us</span></nav>
  <div class="footer-bottom"><span>Copyright 2024 Podiatry. All Rights Reserved.</span><div class="social"><i></i><i></i></div><span>Site by Podiatry Studio</span></div>
</footer>

</body>
</html>
```